125th Church Anniversary Invitation

We are celebrating our 125th Anniversary of the church
We have decided to host a gala event next year (9/30/18) to celebrate this historical anniversary.
We need the invitation and the flyer to communicate the details for the gala and sell ads for the souvenir book. This invitation will be sent to potential guests as well as potential ad purchasers.
The tickets that are distributed primary purpose is:
- Allow us to attain demographical information so that we can send a more formal invitation next year. This will give the guest a tax deductible record of the transaction.

Target Market(s)

Church members. Majority of the people that will receive the invitation are between the ages of 50-80.

Industry/Entity Type

Church

Font styles to use
Serif
Decorative
Script

Colors
b768aa
a64599
d3a5cc
3176b5
fbf289

Requirements
Must have
• I would like a universal look that can be applied to items:
• - Invitation (5.63 x 4.14) primary format
• - event tickets prorated similar look
• - editable texts so that the committee can make changes before it is printed.
• I would like to have our Logo integrated and or our church with religious background
• Sophisticated background
Nice to have
• Please look at the pdf with examples of other church invitations that I like.
Should not have
• Should not be too youthful. The audience is primarily older church members.

```html
<!DOCTYPE html>
<html lang="en">
<head>
<meta charset="UTF-8">
<title>125th Anniversary Gala Invitation</title>
<link href="https://fonts.googleapis.com/css2?family=Great+Vibes&family=Playfair+Display:ital,wght@0,700;1,700&family=Open+Sans:wght@300;400&family=Montserrat:wght@700&display=swap" rel="stylesheet">
<style>
  :root{
    --stage:#bcdcdf;
    --purple:#9a2fa6;
    --purple-deep:#7a1f8a;
    --lilac:#d3a5cc;
    --gold:#e8b73a;
    --gold-light:#fbf289;
    --ink-dark:#1c1218;
    --white:#ffffff;
    --crop-red:#e0262c;
  }
  html,body{margin:0;padding:0;width:1200px;height:1030px;overflow:hidden;background:var(--stage);}
  .invitation{
    position:absolute;left:145px;top:50px;width:910px;height:910px;overflow:hidden;
    box-shadow:0 12px 30px rgba(0,0,0,.25);
  }
  .backdrop{position:absolute;inset:0;
    background:
      radial-gradient(circle at 18% 62%, rgba(255,244,220,.95) 0, rgba(255,220,160,.5) 14%, transparent 34%),
      linear-gradient(160deg,#f4c78e 0%,#e9b184 30%,#a06b6e 55%,#4a2a3e 78%,#1c1218 100%);}
  .crop-line{position:absolute;background:var(--crop-red);}
  .crop-h{left:0;top:150px;width:360px;height:3px;}
  .crop-v{left:805px;top:0;width:3px;height:70px;}
  .crop-h2{left:690px;top:40px;width:220px;height:3px;}
  .ribbon{position:absolute;left:-90px;top:520px;width:640px;height:48px;transform:rotate(-62deg);transform-origin:left center;
    background:linear-gradient(180deg,var(--gold-light),var(--gold) 55%,#b9862a);
    display:flex;align-items:center;justify-content:center;
    font-family:"Playfair Display",serif;font-style:italic;font-weight:700;font-size:22px;color:#3a2410;
    box-shadow:0 3px 8px rgba(0,0,0,.3);}
  .seal{position:absolute;left:300px;top:95px;width:250px;height:250px;border-radius:50%;background:var(--purple);
    display:flex;align-items:center;justify-content:center;z-index:2;}
  .seal-inner{width:180px;height:180px;border-radius:50%;background:var(--white);
    display:flex;flex-direction:column;align-items:center;justify-content:center;}
  .seal-kicker{font-family:"Great Vibes",cursive;font-size:26px;color:#d33a8a;line-height:1;}
  .seal-number{font-family:"Playfair Display",serif;font-weight:700;font-size:70px;color:var(--purple-deep);line-height:1;}
  .seal-number sup{font-size:34px;}
  .banner{position:absolute;left:270px;top:300px;width:540px;height:150px;background:var(--purple);
    outline:3px dotted var(--white);outline-offset:-10px;z-index:1;
    display:flex;align-items:center;justify-content:center;}
  .banner-title{font-family:"Great Vibes",cursive;font-size:96px;color:var(--gold-light);
    text-shadow:0 2px 0 #b9862a;padding-top:30px;}
  .on-label{position:absolute;left:330px;top:535px;font-family:"Open Sans",sans-serif;font-weight:300;font-size:44px;color:var(--white);}
  .date-badge{position:absolute;left:430px;top:490px;width:150px;height:150px;border-radius:50%;
    border:3px dotted var(--white);display:flex;align-items:center;justify-content:center;}
  .date-core{width:130px;height:130px;border-radius:50%;background:var(--purple-deep);
    display:flex;flex-direction:column;align-items:center;justify-content:center;
    font-family:"Open Sans",sans-serif;color:var(--white);font-size:26px;line-height:1.15;}
  .date-core sup{font-size:14px;}
  .venue{position:absolute;left:620px;top:500px;width:270px;color:var(--white);font-family:"Open Sans",sans-serif;}
  .venue-at{font-size:16px;font-weight:300;}
  .venue-name{font-size:28px;font-weight:300;margin:2px 0 10px;}
  .venue-time{font-size:15px;margin:3px 0;}
  .venue-time b{color:var(--gold);font-weight:400;margin-right:8px;}
  .gala{position:absolute;left:70px;top:720px;}
  .gala-word{font-family:"Montserrat",sans-serif;font-weight:700;font-size:90px;letter-spacing:2px;line-height:1;
    background:linear-gradient(90deg,var(--white) 0 30%,var(--gold) 30% 100%);-webkit-background-clip:text;background-clip:text;color:transparent;}
  .gala-sub{font-family:"Open Sans",sans-serif;font-weight:300;font-size:58px;color:var(--white);line-height:1;margin-left:60px;}
</style>
</head>
<body>
  <main class="invitation">
    <div class="backdrop" role="img" aria-label="Sunset church photograph with a cross glowing in warm light fading to dark purple"></div>
    <span class="crop-line crop-h"></span>
    <span class="crop-line crop-v"></span>
    <span class="crop-line crop-h2"></span>

    <div class="ribbon">We've Come This Far by Faith... with God</div>

    <div class="seal">
      <div class="seal-inner">
        <span class="seal-kicker">Celebrating</span>
        <span class="seal-number">125<sup>th</sup></span>
      </div>
    </div>
    <div class="banner"><span class="banner-title">Anniversary</span></div>

    <span class="on-label">On</span>
    <div class="date-badge">
      <div class="date-core"><span>30<sup>th</sup> Sept</span><span>2018</span></div>
    </div>

    <div class="venue">
      <div class="venue-at">at</div>
      <div class="venue-name">Grand Meridian Hotel</div>
      <p class="venue-time"><b>7:00PM</b>Welcome Reception</p>
      <p class="venue-time"><b>8:00PM</b>Dinner</p>
    </div>

    <div class="gala">
      <div class="gala-word">GALA</div>
      <div class="gala-sub">Event</div>
    </div>
  </main>
</body>
</html>
```